Business Cards

We were billed for this because the project timed out. Please give me another designed to open this back up. I was not happy with the last designs (that I was charged for).
we are also using the logo with Clear Water Care for Every Backyard
Also want to utilize Where Healthy Water is our Commitment.

Contact Information for Business Card

Marlowe Stone Group Inc

```html
<!DOCTYPE html>
<html lang="en">
<head>
<meta charset="utf-8">
<title>Marlowe Stone Group – Business Cards</title>
<link rel="stylesheet" href="https://fonts.googleapis.com/css2?family=Montserrat:wght@400;500;800&display=swap">
<style>
  :root {
    --backdrop: #e4e4e9;
    --card-white: #ffffff;
    --brand-blue: #0569b1;
    --sky-blue: #3d9ad8;
    --ink: #444446;
    --ink-soft: #555558;
    --divider: #dcdcdc;
  }
  * { margin: 0; padding: 0; box-sizing: border-box; }
  html, body { width: 1145px; height: 1200px; overflow: hidden; }
  body {
    background: var(--backdrop);
    font-family: "Montserrat", sans-serif;
    position: relative;
  }
  .card {
    position: absolute;
    width: 729px;
    height: 416px;
    border-radius: 46px;
    overflow: hidden;
  }
  .card--front { left: 222px; top: 102px; background: var(--card-white); }
  .card--back { left: 219px; top: 618px; background: var(--brand-blue); color: #fff; }

  .brand { position: absolute; left: 0; right: 0; text-align: center; }
  .brand__dot {
    display: block; margin: 0 auto;
    width: 50px; height: 50px; border-radius: 50%;
  }
  .brand__name {
    display: block;
    font-weight: 800; font-size: 33px; letter-spacing: 2.4px;
    white-space: nowrap; line-height: 1;
  }
  .brand__tagline {
    display: block;
    font-weight: 500; font-size: 14px; letter-spacing: 4.2px;
    white-space: nowrap; margin-top: 5px;
  }
  .card--front .brand { top: 40px; }
  .card--front .brand__dot { background: var(--brand-blue); margin-bottom: 18px; }
  .card--front .brand__name, .card--front .brand__tagline { color: var(--ink); }
  .card--back .brand { top: 132px; }
  .card--back .brand__dot { background: #fff; margin-bottom: 20px; }

  .rule { position: absolute; left: 0; right: 0; top: 184px; height: 7px; background: var(--brand-blue); }

  .person { position: absolute; right: 414px; top: 236px; text-align: right; }
  .person__name { font-size: 41px; font-weight: 500; color: var(--sky-blue); white-space: nowrap; line-height: 1.1; }
  .person__name b { font-weight: 500; color: var(--brand-blue); }
  .person__role { font-size: 13.5px; color: var(--ink-soft); margin-top: 6px; }

  .divider { position: absolute; left: 335px; top: 224px; width: 2px; height: 153px; background: var(--divider); }

  .contacts { position: absolute; left: 356px; top: 234px; }
  .contacts__spine { position: absolute; left: 16px; top: 20px; width: 3px; height: 100px; background: var(--ink); }
  .contact { position: absolute; left: 0; display: flex; align-items: flex-start; }
  .contact--phone { top: 0; }
  .contact--web { top: 49px; }
  .contact--place { top: 99px; }
  .icon {
    width: 35px; height: 35px; border-radius: 6px;
    background: var(--sky-blue);
    display: flex; align-items: center; justify-content: center;
    position: relative; z-index: 1; flex: none;
  }
  .icon--dark { background: var(--brand-blue); }
  .contact__lines { margin-left: 18px; margin-top: -3px; font-size: 16.5px; line-height: 20.5px; color: var(--ink); white-space: nowrap; }

  .back-web { position: absolute; left: 218px; top: 290px; display: flex; align-items: center; }
  .back-web .icon { background: var(--sky-blue); }
  .back-web__url { margin-left: 18px; font-size: 16.5px; color: #fff; }
</style>
</head>
<body>

<section class="card card--front" aria-label="Business card front">
  <div class="brand">
    <span class="brand__dot"></span>
    <span class="brand__name">MARLOWE STONE GROUP</span>
    <span class="brand__tagline">CLEAR WATER CARE FOR EVERY BACKYARD</span>
  </div>
  <div class="rule"></div>

  <div class="person">
    <p class="person__name">Dara <b>Nolen</b></p>
    <p class="person__role">Founder/Director</p>
  </div>
  <div class="divider"></div>

  <div class="contacts">
    <div class="contacts__spine"></div>
    <div class="contact contact--phone">
      <span class="icon">
        <svg width="16" height="16" viewBox="0 0 24 24" fill="#fff" aria-hidden="true"><path d="M6.6 10.8a15.1 15.1 0 0 0 6.6 6.6l2.2-2.2c.3-.3.7-.4 1-.2 1.1.4 2.3.6 3.6.6.6 0 1 .4 1 1V20c0 .6-.4 1-1 1C10.6 21 3 13.4 3 4c0-.6.4-1 1-1h3.5c.6 0 1 .4 1 1 0 1.3.2 2.5.6 3.6.1.3 0 .7-.2 1z"/></svg>
      </span>
      <p class="contact__lines">+000 000 000 000<br>+000 000 000 000</p>
    </div>
    <div class="contact contact--web">
      <span class="icon icon--dark">
        <svg width="17" height="17" viewBox="0 0 24 24" fill="none" stroke="#fff" stroke-width="2" aria-hidden="true"><circle cx="12" cy="12" r="9"/><path d="M3 12h18M12 3c3 3.2 3 14.8 0 18M12 3c-3 3.2-3 14.8 0 18"/></svg>
      </span>
      <p class="contact__lines">hello@marlowestonegroup.com<br>www.marlowestonegroup.com</p>
    </div>
    <div class="contact contact--place">
      <span class="icon">
        <svg width="14" height="16" viewBox="0 0 24 24" fill="#fff" aria-hidden="true"><path d="M12 2a7 7 0 0 0-7 7c0 5.2 7 13 7 13s7-7.8 7-13a7 7 0 0 0-7-7zm0 9.5A2.5 2.5 0 1 1 12 6.5a2.5 2.5 0 0 1 0 5z"/></svg>
      </span>
      <p class="contact__lines">La, Street<br>Location</p>
    </div>
  </div>
</section>

<section class="card card--back" aria-label="Business card back">
  <div class="brand">
    <span class="brand__dot"></span>
    <span class="brand__name">MARLOWE STONE GROUP</span>
    <span class="brand__tagline">CLEAR WATER CARE FOR EVERY BACKYARD</span>
  </div>
  <div class="back-web">
    <span class="icon">
      <svg width="17" height="17" viewBox="0 0 24 24" fill="none" stroke="#fff" stroke-width="2" aria-hidden="true"><circle cx="12" cy="12" r="9"/><path d="M3 12h18M12 3c3 3.2 3 14.8 0 18M12 3c-3 3.2-3 14.8 0 18"/></svg>
    </span>
    <span class="back-web__url">www.marlowestonegroup.com</span>
  </div>
</section>

</body>
</html>
```